BRIGHTDESK - Remote Tech Support Site

We are looking for a new very responsive and simple website for our brand Brightdesk.example - a remote technical support company.

This company supports customers Globally in different countries throughout Eur/ North America / South America / Asia etc (please keep this in mind and integrate into the idea).

Its important to us that the design is very explanatory, the customer should easily be able to figure out that we provide computer support right away ... I like one page responsive type designs as well without a bunch of menu items

Here are some similar sites we like - but still looking for a unique design that fits out brand "brightdesk" - I have upload also some layouts i like (but the designs are not important just the layouts), youll see it includes consumer business etc which is important.

PLOVE.EXAMPLE - I love how clean it is - nice and white easy to see everything

ZENBYTE247.EXAMPLE - also nice the layout and responsive one page design makes it easy to use

lumacorefix.example - similar to zenbyte design as well - you can get the idea im looking for between the two

You will notice those examples are much different then the attachments I added - again this is more of an idea for possible layouts .. attached is also the logo - could inspire color scheme / blue white black etc

Target Market(s)

Home consumers without computer knowledge , older age 45-65, small medium business ... computer repair - slow computers

Industry/Entity Type

Computer Repair

Logo Text

Brightdesk

Coding

Coded - Design and coding required

Number of Pages Required

1 page

Font styles to use
Sans Serif
Other font styles liked:
• your choice responsive

Colors

Designer to choose colors to be used in the design.

Requirements
Must have
• Clean - responsive - professional design - the name says it all - brightdesk
• CALL TO ACTIONS FOR "Get Help Now!" / "Learn More" etc
Nice to have
• We are looking for a new very responsive and simple website for our brand Brightdesk.example - a remote technical support company.
• This company supports customers Globally in different countries throughout Eur/ North America / South America / Asia etc (please keep this in mind and integrate into the idea).
• Its important to us that the design is very explanatory, the customer should easily be able to figure out that we provide computer support right away ... I like one page responsive type designs as well without a bunch of menu items
• Here are some similar sites we like - but still looking for a unique design that fits out brand "brightdesk" - I have upload also some layouts i like (but the designs are not important just the layouts), youll see it includes consumer business etc which is important.
• PLOVE.EXAMPLE - I love how clean it is - nice and white easy to see everything
• ZENBYTE247.EXAMPLE - also nice the layout and responsive one page design makes it easy to use
• lumacorefix.example - similar to zenbyte design as well - you can get the idea im looking for between the two
Should not have
• dark, packed page - bad small font -

```html
<!DOCTYPE html>
<html lang="en">
<head>
<meta charset="utf-8">
<title>Brightdesk – Remote Tech Support</title>
<link rel="stylesheet" href="https://fonts.googleapis.com/css2?family=Open+Sans:wght@300;400;600;700&display=swap">
<style>
:root{
  --ink:#222;
  --text:#444;
  --muted:#777;
  --line:#d9d9d9;
  --blue:#2f7fe0;
  --blue-deep:#2575d6;
  --blue-tab:#3d8fe8;
  --link:#2a78d6;
  --green:#2f8f2f;
  --btn-blue:#3a78f2;
  --panel:#f7f7f7;
  --table-grey:#f4f4f4;
  --warm:#efebe5;
  --footer:#f1f1f1;
  --white:#fff;
}
*{box-sizing:border-box;margin:0;padding:0}
html,body{width:1200px;height:3289px;overflow:hidden}
body{position:relative;background:var(--white);font-family:"Open Sans",Arial,sans-serif;color:var(--text)}
.abs{position:absolute}
a{color:inherit;text-decoration:none}

/* top bar */
.topbar{left:0;top:0;width:1200px;height:31px;font-size:11px;color:var(--text)}
.topbar .region{left:159px;top:8px;display:flex;align-items:center;gap:6px}
.topbar .signin{left:990px;top:8px;display:flex;align-items:center;gap:6px}

/* nav */
.nav{left:0;top:31px;width:1200px;height:62px;border-top:1px solid #eee}
.brand{display:flex;align-items:center;gap:7px;font-size:22px;font-weight:400;color:var(--ink);letter-spacing:-.3px}
.brand .dot{width:24px;height:24px;border-radius:50%;background:var(--ink)}
.nav .brand{left:159px;top:16px}
.menu{left:313px;top:22px;display:flex;gap:17px;font-size:11.5px;color:var(--ink)}
.talk{left:860px;top:8px;width:181px;text-align:right}
.talk small{display:block;font-size:11px;color:var(--text)}
.talk strong{display:block;font-size:20px;font-weight:400;color:var(--ink);margin-top:1px}

/* hero */
.hero{left:0;top:93px;width:1200px;height:375px;background:linear-gradient(90deg,#dfeaf1 0%,#e6eff5 45%,#eef3f6 100%)}
.hero-photo{left:520px;top:0;width:680px;height:375px;background:linear-gradient(90deg,rgba(230,239,245,0) 0%,#cfdde7 25%,#9fb4c6 55%,#c9d6e0 80%,#e8eef2 100%)}
.hero h1{left:159px;top:84px;font-size:37px;font-weight:300;line-height:46px;color:var(--ink)}
.hero p{left:159px;top:184px;font-size:16px;line-height:22px;color:var(--ink)}
.btn{display:flex;align-items:center;justify-content:center;color:var(--white);font-size:10.5px;font-weight:600;letter-spacing:.3px}
.btn-green{background:var(--green)}
.hero .btn{left:159px;top:247px;width:163px;height:40px}

/* service cards */
.card{top:507px;width:181px}
.card .shot{width:181px;height:137px}
.card h3{margin-top:20px;font-size:13px;font-weight:400;color:var(--ink)}
.card p{margin-top:4px;font-size:10.5px;line-height:14px;color:var(--text)}
.card a{display:block;margin-top:14px;font-size:10px;color:var(--link)}

/* how it works */
.how{left:0;top:779px;width:1200px;height:313px;background:var(--panel)}
.section-title{width:1200px;left:0;text-align:center;font-size:24px;font-weight:300;color:var(--ink)}
.how .section-title{top:38px}
.how .lead{left:330px;top:83px;width:540px;text-align:center;font-size:10.5px;line-height:15px}
.step{top:172px;width:250px;text-align:center}
.step svg{display:block;margin:0 auto}
.step h4{margin-top:12px;font-size:13px;font-weight:400;color:var(--link)}
.step p{margin-top:6px;font-size:10px;line-height:14px;color:var(--text)}

/* plans */
.plans .section-title{top:1160px}
.plans .lead{left:380px;top:1224px;width:440px;text-align:center;font-size:10.5px;line-height:15px;color:var(--text)}
.plans .lead b{color:var(--ink)}
.plans .all{left:0;top:1268px;width:1200px;text-align:center;font-size:10.5px;color:var(--link)}
.tab{left:668px;top:1341px;width:194px;height:44px;background:var(--blue-tab);color:var(--white);font-size:11px;display:flex;align-items:center;justify-content:center}
.col-bg{top:1385px;height:561px}
.col-premium{left:490px;width:178px;background:var(--table-grey)}
.col-popular{left:668px;width:194px;background:var(--blue-deep)}
.col-platinum{left:862px;width:179px;background:var(--table-grey)}
.price{top:1400px;text-align:center}
.price h5{font-size:15px;font-weight:400;color:var(--ink)}
.price .amt{margin-top:4px;font-size:29px;font-weight:300;color:var(--ink)}
.price .amt sup{font-size:14px;vertical-align:12px}
.price .amt small{font-size:9px}
.col-popular-txt h5,.col-popular-txt .amt{color:var(--white)}
.head-rule{left:159px;top:1474px;width:882px;height:1px;background:var(--line)}
.foot-rule{left:159px;top:1946px;width:331px;height:1px;background:var(--line)}
.row{left:159px;width:882px;display:flex}
.row .feat{width:331px;padding-right:20px;font-size:10px;line-height:13px;color:var(--text)}
.row .feat b{color:var(--ink);font-weight:700}
.row .cell{display:flex;justify-content:center;padding-top:8px}
.row .c1{width:178px}.row .c2{width:194px}.row .c3{width:179px}
.row-line{left:159px;width:331px;height:1px;background:#ececec}

/* cta band */
.cta{left:0;top:2007px;width:1200px;height:376px;background:var(--warm)}
.cta-photo{left:0;top:0;width:600px;height:376px;background:linear-gradient(90deg,#f1ede6 0%,#e9dfc9 40%,#d8c27a 58%,#e7e2da 80%,#efebe5 100%)}
.cta h2{left:562px;top:96px;width:460px;font-size:28px;font-weight:300;line-height:34px;color:var(--ink)}
.cta p{left:562px;top:180px;width:430px;font-size:11.5px;line-height:16px;color:var(--text)}
.cta .btn{left:562px;top:261px;width:165px;height:40px}
.cta .powered{left:562px;top:314px;font-size:9px;color:var(--ink)}
.cta .powered b{font-size:11px}

/* booking */
.book h2{left:159px;top:2432px;width:340px;font-size:30px;font-weight:300;line-height:40px;color:var(--ink)}
.book .lead{left:159px;top:2533px;width:345px;font-size:10.5px;line-height:15px}
.lbl{font-size:10px;color:var(--ink)}
.field{height:30px;border:1px solid #bdbdbd;background:var(--white);font-size:10px;color:#999;display:flex;align-items:center;padding:0 8px;gap:6px}
.book .btn-book{left:159px;top:2868px;width:344px;height:30px;background:var(--btn-blue);color:var(--white);font-size:11px;display:flex;align-items:center;justify-content:center}
.optin{left:159px;top:2912px;font-size:10px;color:var(--ink);display:flex;align-items:center;gap:6px}
.optin i{width:11px;height:11px;border:1px solid #888;display:block}

.review{left:565px;top:2440px;width:476px;height:454px;background:var(--white);box-shadow:0 1px 8px rgba(0,0,0,.14)}
.review h3{position:absolute;left:0;top:34px;width:476px;text-align:center;font-size:18px;font-weight:400;color:var(--ink)}
.review .badge{left:183px;top:84px;width:110px;height:12px;background:#e1e1e1;border-radius:2px}
.review .rating{left:183px;top:108px;width:110px;height:22px;background:#00b67a}
.review .avatar{left:174px;top:156px;width:128px;height:128px;border-radius:50%;background:radial-gradient(circle at 50% 40%,#d9d4cf,#9aa4ad)}
.review .name{left:0;top:314px;width:476px;text-align:center;font-size:13px;color:var(--ink)}
.review .from{left:0;top:334px;width:476px;text-align:center;font-size:10px;color:var(--muted)}
.review blockquote{position:absolute;left:48px;top:360px;width:380px;text-align:center;font-size:14.5px;line-height:20px;color:var(--ink)}

/* footer */
.footer{left:0;top:3000px;width:1200px;height:243px;background:var(--footer)}
.footer .brand{position:absolute;left:159px;top:52px;font-size:20px;color:#555}
.footer .brand .dot{width:22px;height:22px;background:#555}
.footer .about{left:159px;top:92px;width:320px;font-size:10.5px;line-height:14px;color:var(--text)}
.fcol{top:82px;font-size:10.5px;line-height:14.5px;color:var(--text)}
.fcol h6{font-size:10.5px;font-weight:400;color:var(--ink)}
.social{display:flex;gap:12px;margin-top:10px}
.social i{width:11px;height:11px;border-radius:50%;background:#9a9a9a;display:block}
.legal{left:0;top:3243px;width:1200px;height:46px;border-top:1px solid #e2e2e2;background:var(--white)}
.legal .row-links{left:159px;top:16px;display:flex;gap:14px;font-size:10px;color:var(--text)}
</style>
</head>
<body>

<!-- top bar -->
<div class="abs topbar">
  <div class="abs region">
    <svg width="12" height="12" viewBox="0 0 12 12" fill="none" stroke="#333" stroke-width="1"><circle cx="6" cy="6" r="5"/><ellipse cx="6" cy="6" rx="2.2" ry="5"/><path d="M1 6h10"/></svg>
    United States (English)
  </div>
  <div class="abs signin">
    <svg width="12" height="12" viewBox="0 0 12 12" fill="none" stroke="#333" stroke-width="1"><circle cx="6" cy="4" r="2.6"/><path d="M1.5 11.5c.6-2.6 2.3-3.8 4.5-3.8s3.9 1.2 4.5 3.8"/></svg>
    Sign in
  </div>
</div>

<!-- navigation -->
<header class="abs nav">
  <div class="abs brand"><span class="dot"></span>brightdesk</div>
  <nav class="abs menu">
    <a>Services ⌄</a><a>Plans</a><a>Company</a><a>Customers</a><a>Contact</a>
  </nav>
  <div class="abs talk"><small>Talk to an expert right now</small><strong>+1 (555) 010 2030</strong></div>
</header>

<!-- hero -->
<section class="abs hero">
  <div class="abs hero-photo" role="img" aria-label="Photo of a man in a blue shirt working on a laptop by a bright window"></div>
  <h1 class="abs">Dedicated support.<br>Anywhere, anytime.</h1>
  <p class="abs">Save up to $90 on an All-devices Platinum plan.<br>Limited-time offer.*</p>
  <a class="abs btn btn-green">GET HELP NOW</a>
</section>

<!-- service cards -->
<div class="abs card" style="left:159px">
  <div class="shot" role="img" aria-label="Photo of a person using a laptop at home" style="background:linear-gradient(135deg,#d9d2c8,#8e8780)"></div>
  <h3>Personal devices</h3>
  <p>We can help you fix your Personal laptop, tablet, desktop or All-in-One computer</p>
  <a>DISCOVER &gt;</a>
</div>
<div class="abs card" style="left:390px">
  <div class="shot" role="img" aria-label="Photo of an office workspace with business devices" style="background:linear-gradient(135deg,#8a8d8c,#cfcac0)"></div>
  <h3>Business devices</h3>
  <p>We can help you fix your Personal laptop, tablet, desktop or All-in-One computer</p>
  <a>DISCOVER &gt;</a>
</div>
<div class="abs card" style="left:631px">
  <div class="shot" role="img" aria-label="Photo of a technician setting up computer hardware" style="background:linear-gradient(135deg,#3f4340,#9c9a86)"></div>
  <h3>Set-up &amp; Installation</h3>
  <p>We can help you fix your Personal laptop, tablet, desktop or All-in-One computer</p>
  <a>DISCOVER &gt;</a>
</div>
<div class="abs card" style="left:862px">
  <div class="shot" role="img" aria-label="Photo of a hand holding a tablet showing a connected screen" style="background:linear-gradient(135deg,#cfd2d0,#6f8f6a)"></div>
  <h3>Internet &amp; Networking</h3>
  <p>We can help you fix your Personal laptop, tablet, desktop or All-in-One computer</p>
  <a>DISCOVER &gt;</a>
</div>

<!-- how it works -->
<section class="abs how">
  <h2 class="abs section-title">So How Does It Work?</h2>
  <p class="abs lead">Our experts will get you a free healthcheck today and you can describe your problem and they'll look for the best solutions. You can also ask to live chat to a person at any time.</p>
  <div class="abs step" style="left:153px">
    <svg width="24" height="24" viewBox="0 0 24 24" fill="none" stroke="#2a78d6" stroke-width="1.5"><path d="M6 3l3 4-2 2c1 2.5 3.5 5 6 6l2-2 4 3-2 3C10 19 5 14 3 5z"/></svg>
    <h4>Reach an expert</h4>
    <p>Our Technology Advisors will talk you through any question or remotely connect to your device to help.</p>
  </div>
  <div class="abs step" style="left:471px">
    <svg width="24" height="24" viewBox="0 0 24 24" fill="none" stroke="#2a78d6" stroke-width="1.5"><path d="M4 7V4h3M17 4h3v3M20 17v3h-3M7 20H4v-3"/><rect x="8" y="8" width="8" height="8"/></svg>
    <h4>Remotely connect</h4>
    <p>Our Technology Advisors will talk you through any question or remotely connect to your device to help.</p>
  </div>
  <div class="abs step" style="left:793px">
    <svg width="24" height="24" viewBox="0 0 24 24"><path d="M12 2l8 3v6c0 5-3.5 9-8 11-4.5-2-8-6-8-11V5z" fill="#2a78d6"/><path d="M12 2v20M4 11h16" stroke="#fff" stroke-width="1.2"/></svg>
    <h4>Select a plan</h4>
    <p>Your chosen service plan will keep you protected and running smoothly with on-going support.</p>
  </div>
</section>

<!-- plans -->
<section class="plans">
  <h2 class="abs section-title">Which plans you need help with?</h2>
  <p class="abs lead">If you are not sure what's the plan you need, call now at <b>+1 (555) 010 2030</b>, an expert will assist you after a free PC Healthcheck.</p>
  <a class="abs all">View all Brightdesk plans</a>

  <div class="abs tab">Most Popular</div>
  <div class="abs col-bg col-premium"></div>
  <div class="abs col-bg col-popular"></div>
  <div class="abs col-bg col-platinum"></div>

  <div class="abs price" style="left:490px;width:178px"><h5>Premium</h5><div class="amt"><sup>$</sup>19,99 <small>per month</small></div></div>
  <div class="abs price col-popular-txt" style="left:668px;width:194px"><h5>Premium+</h5><div class="amt"><sup>$</sup>29,99 <small>per month</small></div></div>
  <div class="abs price" style="left:862px;width:179px"><h5>Platinium</h5><div class="amt"><sup>$</sup>39,99 <small>per month</small></div></div>
  <div class="abs head-rule"></div>

  <svg width="0" height="0" style="position:absolute">
    <defs>
      <path id="tick" d="M1 7l4.5 4.5L15 2" fill="none" stroke-width="1.4"/>
    </defs>
  </svg>

  <div class="abs row" style="top:1488px;height:62px">
    <div class="feat"><b>Help &amp; Support from certified IT professionals</b><br>We help fixing issues in your computer. All your questions answered!</div>
    <div class="cell c1"><svg width="16" height="14"><use href="#tick" stroke="#222"/></svg></div>
    <div class="cell c2"><svg width="16" height="14"><use href="#tick" stroke="#fff"/></svg></div>
    <div class="cell c3"><svg width="16" height="14"><use href="#tick" stroke="#222"/></svg></div>
  </div>
  <div class="abs row-line" style="top:1550px"></div>
  <div class="abs row" style="top:1550px;height:40px">
    <div class="feat"><b>Response time (from ticket creation)</b><br>Our response to your computer issues or problems</div>
    <div class="cell c1"><svg width="16" height="14"><use href="#tick" stroke="#222"/></svg></div>
    <div class="cell c2"><svg width="16" height="14"><use href="#tick" stroke="#fff"/></svg></div>
    <div class="cell c3"><svg width="16" height="14"><use href="#tick" stroke="#222"/></svg></div>
  </div>
  <div class="abs row-line" style="top:1590px"></div>
  <div class="abs row" style="top:1590px;height:48px">
    <div class="feat"><b>Award Winning Security software</b> to protect your PC against all kind of Internet threats.</div>
    <div class="cell c1"><svg width="16" height="14"><use href="#tick" stroke="#222"/></svg></div>
    <div class="cell c2"><svg width="16" height="14"><use href="#tick" stroke="#fff"/></svg></div>
    <div class="cell c3"><svg width="16" height="14"><use href="#tick" stroke="#222"/></svg></div>
  </div>
  <div class="abs row-line" style="top:1638px"></div>
  <div class="abs row" style="top:1638px;height:58px">
    <div class="feat"><b>OnlineBackUp</b> to secure and automated backup and store of all your most important memories and files (GB below)</div>
    <div class="cell c1"><svg width="16" height="14"><use href="#tick" stroke="#222"/></svg></div>
    <div class="cell c2"><svg width="16" height="14"><use href="#tick" stroke="#fff"/></svg></div>
    <div class="cell c3"><svg width="16" height="14"><use href="#tick" stroke="#222"/></svg></div>
  </div>
  <div class="abs row-line" style="top:1696px"></div>
  <div class="abs row" style="top:1696px;height:57px">
    <div class="feat"><b>Tranferable Subscription</b> to a another computer quickly, easily and for free</div>
    <div class="cell c1"></div>
    <div class="cell c2"><svg width="16" height="14"><use href="#tick" stroke="#fff"/></svg></div>
    <div class="cell c3"><svg width="16" height="14"><use href="#tick" stroke="#222"/></svg></div>
  </div>
  <div class="abs row-line" style="top:1753px"></div>
  <div class="abs row" style="top:1753px;height:62px">
    <div class="feat"><b>Upgrade Guarantee</b><br>Freeaccess to all software, feature and service upgrades and enhancements throughout complete subscription period</div>
    <div class="cell c1"></div>
    <div class="cell c2"><svg width="16" height="14"><use href="#tick" stroke="#fff"/></svg></div>
    <div class="cell c3"><svg width="16" height="14"><use href="#tick" stroke="#222"/></svg></div>
  </div>
  <div class="abs row-line" style="top:1815px"></div>
  <div class="abs row" style="top:1815px;height:57px">
    <div class="feat"><b>Software install &amp; uninstall service</b><br>We install new products you might have purchased and make sure installation goes correct.</div>
    <div class="cell c1"></div>
    <div class="cell c2"><svg width="16" height="14"><use href="#tick" stroke="#fff"/></svg></div>
    <div class="cell c3"><svg width="16" height="14"><use href="#tick" stroke="#222"/></svg></div>
  </div>
  <div class="abs row-line" style="top:1872px"></div>
  <div class="abs row" style="top:1872px;height:74px">
    <div class="feat"><b>Personal IT Supporter</b><br>Throughout your entire subscription period you will always have the same IT supporter allocated to you in order to secure the best, fastest and most continuous service possible</div>
    <div class="cell c1"></div>
    <div class="cell c2"></div>
    <div class="cell c3" style="padding-top:22px"><svg width="16" height="14"><use href="#tick" stroke="#222"/></svg></div>
  </div>
  <div class="abs foot-rule"></div>
</section>

<!-- call to action band -->
<section class="abs cta">
  <div class="abs cta-photo" role="img" aria-label="Photo of a happy woman in a yellow top raising her hands in front of a laptop"></div>
  <h2 class="abs">Reach us and we will do the job for you - immediately</h2>
  <p class="abs">You can always count on personalized, 1-on-1 service. We'll pair you with a knowledgeable advisor that you can get to know and trust. They will help you fix errors and solve issues remotely, fast easy and hassle free on any device.</p>
  <a class="abs btn btn-green">GET HELP NOW</a>
  <div class="abs powered">Powered by <b>RemoteLink</b></div>
</section>

<!-- booking form -->
<section class="book">
  <h2 class="abs">Book your free PC diagnostic check</h2>
  <p class="abs lead">Our experts will get you a free healthcheck today and you can describe your problem and they'll look for the best solutions. You can also ask to live chat to a person at any time.</p>

  <label class="abs lbl" style="left:159px;top:2614px">First name</label>
  <div class="abs field" style="left:159px;top:2628px;width:163px"></div>
  <label class="abs lbl" style="left:329px;top:2614px">Last name</label>
  <div class="abs field" style="left:329px;top:2628px;width:174px"></div>

  <label class="abs lbl" style="left:159px;top:2676px">Email address</label>
  <div class="abs field" style="left:159px;top:2690px;width:344px">Someone@example.com</div>

  <label class="abs lbl" style="left:159px;top:2740px">Phone number</label>
  <div class="abs field" style="left:159px;top:2754px;width:344px;color:#333">
    <svg width="18" height="12" viewBox="0 0 18 12"><rect width="18" height="12" fill="#c33"/><rect y="2" width="18" height="2" fill="#fff"/><rect y="6" width="18" height="2" fill="#fff"/><rect y="10" width="18" height="2" fill="#fff"/><rect width="8" height="7" fill="#2a4aa0"/></svg>
    +1 ⌄
  </div>

  <label class="abs lbl" style="left:159px;top:2804px">Preferred time of day for us to contact you</label>
  <div class="abs field" style="left:159px;top:2818px;width:344px;justify-content:space-between">Anytime of the day <span style="color:#555">⌄</span></div>

  <a class="abs btn-book">Book now</a>
  <div class="abs optin"><i></i>Send me offers from Brightdesk. You can unsubscribe at any time.</div>

  <div class="abs review">
    <h3>Review &amp; Feedback</h3>
    <div class="abs badge"></div>
    <div class="abs rating"></div>
    <div class="abs avatar" role="img" aria-label="Portrait photo of the reviewer"></div>
    <div class="abs name">Henri M.</div>
    <div class="abs from">France</div>
    <blockquote>"It was a huge help and relief to find out that there are profesionals who are can save me from hours of frustriation. I think I can fairly say it's one of the best technical support I can count on."</blockquote>
  </div>
</section>

<!-- footer -->
<footer class="abs footer">
  <div class="brand"><span class="dot"></span>brightdesk</div>
  <p class="abs about">We are a group of technicians who work round the clock to ensure that your PC works perfectly. Get your computer free of suspicious software and have a healthy system.<br><br>You can get in touch with us any time of the day, any day of the week. We offer support through phone and online chat.</p>
  <div class="abs fcol" style="left:503px"><h6>Services</h6>Personal devices<br>Business devices<br>Set-up &amp; Installation<br>Internet &amp; Networking</div>
  <div class="abs fcol" style="left:684px"><h6>Plans</h6>Premium<br>Premium+<br>Platinium<br>Business</div>
  <div class="abs fcol" style="left:818px"><h6>Contact</h6>info@brightdesk.example<br>+1 555 0199 0<br>
    <div class="social"><i></i><i></i><i></i><i></i></div>
  </div>
</footer>
<div class="abs legal">
  <div class="abs row-links"><span>© 2017 Brightdesk, Inc.</span><span>Terms &amp; Conditions</span><span>Refund Policy</span><span>Privacy</span></div>
</div>

</body>
</html>
```